Business Card Design Project

I want a design for my business cards based on an excisting logo design.

Target Market(s)

Marketeers, PR-peeps, CEO's, decisionmakers, entrepreneurs

Industry/Entity Type

Business

Requirements
Nice to have
• Some visual interest on the back too
Should not have
• Sarif on the font

```html
<!DOCTYPE html>
<html lang="nl">
<head>
<meta charset="utf-8">
<title>LeafLine PR – Business Cards</title>
<link rel="stylesheet" href="https://fonts.googleapis.com/css2?family=Questrial&display=swap">
<style>
  :root {
    --backdrop: #e4e4e2;
    --card-dark: #2a2625;
    --card-dark-edge: #1f1c1b;
    --card-light: #ffffff;
    --leaf-green: #7cc242;
    --deep-green: #1e8f3a;
    --mid-green: #4fae3f;
    --ink-light: #f2f2f2;
    --ink-dark: #222222;
    --ink-grey: #6d6d6d;
    --band-grey: #d9d9d9;
  }
  * { box-sizing: border-box; margin: 0; padding: 0; }
  html, body {
    width: 1200px; height: 951px; overflow: hidden;
    background: var(--backdrop);
    font-family: "Questrial", "Century Gothic", sans-serif;
  }
  .canvas { position: relative; width: 1200px; height: 951px; }

  .card {
    position: absolute;
    width: 580px; height: 340px;
    border-radius: 22px;
    overflow: hidden;
    box-shadow: 0 10px 30px rgba(0,0,0,.18);
  }

  /* Back of the card */
  .card-back {
    left: 80px; top: 100px;
    background: radial-gradient(circle at 50% 40%, #332e2d 0%, var(--card-dark) 55%, var(--card-dark-edge) 100%);
    color: var(--ink-light);
    text-align: center;
  }
  .card-back .brand-mark {
    width: 96px; height: 96px; border-radius: 50%;
    background: var(--leaf-green);
    margin: 58px auto 22px;
  }
  .card-back .brand-name {
    font-size: 42px; letter-spacing: 1px; color: var(--ink-light);
  }
  .card-back .tagline {
    position: absolute; left: 0; right: 0; bottom: 36px;
    font-size: 16px; letter-spacing: .4px; color: var(--ink-light);
  }

  /* Front of the card */
  .card-front {
    left: 540px; top: 500px;
    background: var(--card-light);
    color: var(--ink-dark);
  }
  .card-front .brand {
    position: absolute; left: 36px; top: 36px;
    display: flex; align-items: center; gap: 10px;
  }
  .card-front .brand-mark {
    width: 40px; height: 40px; border-radius: 50%; background: var(--leaf-green);
  }
  .card-front .brand-name { font-size: 22px; color: var(--ink-grey); }

  .contact {
    position: absolute; left: 320px; top: 40px;
    list-style: none; font-size: 16px; line-height: 1.25;
  }
  .contact li { display: flex; align-items: flex-start; gap: 10px; margin-bottom: 4px; }
  .contact svg { flex: none; width: 16px; height: 16px; margin-top: 1px; }
  .contact .icon { fill: var(--mid-green); }

  .person { position: absolute; left: 36px; top: 160px; }
  .person .name { font-size: 22px; margin-bottom: 16px; }
  .person .social { font-size: 17px; line-height: 1.2; color: var(--ink-dark); }

  .swoosh { position: absolute; left: 0; bottom: 0; width: 580px; height: 120px; }
</style>
</head>
<body>
<main class="canvas">

  <section class="card card-back" aria-label="Card back">
    <div class="brand-mark"></div>
    <div class="brand-name">LeafLine PR</div>
    <p class="tagline">Systemisch en strategisch PR • Marketing • En communicatieadvies</p>
  </section>

  <section class="card card-front" aria-label="Card front">
    <div class="brand">
      <span class="brand-mark"></span>
      <span class="brand-name">LeafLine PR</span>
    </div>

    <ul class="contact">
      <li>
        <svg viewBox="0 0 16 16"><path class="icon" d="M8 1 1 7.5h2.2V15h3.6v-4.5h2.4V15h3.6V7.5H15z"/></svg>
        <span>Lindelaan 12<br>6712 AB Ede</span>
      </li>
      <li>
        <svg viewBox="0 0 16 16"><path class="icon" d="M4.2 1.5 6.4 4 5.1 5.6c.9 2 2.4 3.5 4.3 4.4l1.5-1.4 2.6 2.2-1.3 2.5C7.5 13.3 2.7 8.6 2 3z"/></svg>
        <span>+31(0)6 12345678</span>
      </li>
      <li>
        <svg viewBox="0 0 16 16"><path class="icon" d="M1.5 4h13v8.5h-13z"/><path d="M1.5 4 8 9l6.5-5" fill="none" stroke="#fff" stroke-width="1.3"/></svg>
        <span>mara.jansen@leaflinepr.nl</span>
      </li>
      <li>
        <svg viewBox="0 0 16 16"><circle class="icon" cx="8" cy="8" r="7"/></svg>
        <span>www.leaflinepr.nl</span>
      </li>
    </ul>

    <div class="person">
      <p class="name">Mara Jansen</p>
      <p class="social">twitter.com/_leaflinepr<br>facebook.com/leaflinepr</p>
    </div>

    <svg class="swoosh" viewBox="0 0 580 120" preserveAspectRatio="none" aria-hidden="true">
      <path d="M0 70 C160 40 340 20 580 10 V120 H0z" fill="var(--band-grey)"/>
      <path d="M0 85 C180 60 360 40 580 35 V120 H0z" fill="var(--leaf-green)"/>
      <path d="M0 100 C200 80 380 65 580 62 V120 H0z" fill="var(--deep-green)"/>
    </svg>
  </section>

</main>
</body>
</html>
```